Global Weight loss program

we need a business card based in Brooklyn , NY called PeppertonRUN . Mara Dulvik Tenbrook the founder and creator of PeppertonRUN Movement. A business based around nutrition, health, Whole Foods and fitness.

Industry/Entity Type

Food Service

Contact Information for Business Card

Phone number : 718-555-0143
website www.peppertonrun.com
email : mara@peppertonrun.com

Font styles to use
Sans Serif

Requirements
Must have
• logo colors
• green black and gold
Nice to have
• must be simple and sharp.
Should not have
• pictures of items

```html
<!DOCTYPE html>
<html lang="en">
<head>
<meta charset="UTF-8">
<title>PeppertonRUN Business Card</title>
<link href="https://fonts.googleapis.com/css2?family=Ubuntu:wght@400;500;700&display=swap" rel="stylesheet">
<style>
  :root {
    --stage: #e9e7e3;
    --card-light: #ffffff;
    --card-dark: #262626;
    --ink: #2b2b2b;
    --ink-soft: #6b6b6b;
    --green: #7cc41f;
    --text-light: #f2f2f2;
    --ghost: #303030;
  }
  * { box-sizing: border-box; margin: 0; padding: 0; }
  html, body {
    width: 1200px; height: 800px; overflow: hidden;
    background: var(--stage);
    font-family: "Ubuntu", sans-serif;
  }
  .stage {
    position: relative; width: 1200px; height: 800px;
    display: flex; align-items: center; justify-content: center; gap: 60px;
  }
  .card {
    position: relative; width: 525px; height: 300px; overflow: hidden;
    box-shadow: 0 10px 28px rgba(0,0,0,0.18);
  }
  .card--front {
    background: var(--card-light);
    display: flex; flex-direction: column; align-items: center; justify-content: center;
  }
  .brand {
    display: flex; align-items: center; gap: 14px;
  }
  .brand__dot {
    width: 30px; height: 30px; border-radius: 50%; background: var(--green);
  }
  .brand__name {
    font-size: 50px; font-weight: 500; color: var(--ink); letter-spacing: -0.5px;
  }
  .tagline {
    margin-top: 8px; font-size: 15px; letter-spacing: 3px; color: var(--ink-soft);
  }
  .card--back { background: var(--card-dark); }
  .card__ghost-mark {
    position: absolute; right: -40px; top: 20px;
    width: 280px; height: 280px; border-radius: 50%; background: var(--ghost);
  }
  .identity { position: absolute; left: 42px; top: 78px; }
  .identity__name { font-size: 23px; font-weight: 500; color: var(--green); }
  .identity__role { margin-top: 6px; font-size: 13px; color: var(--text-light); letter-spacing: 0.5px; }
  .contact { position: absolute; left: 42px; top: 168px; list-style: none; }
  .contact__item {
    display: flex; align-items: center; gap: 12px;
    font-size: 15px; color: var(--text-light); line-height: 22px;
  }
  .contact__icon { width: 14px; height: 14px; fill: var(--green); flex: none; }
  .card__stripe {
    position: absolute; left: 0; right: 0; bottom: 20px; height: 5px; background: var(--green);
  }
</style>
</head>
<body>
<main class="stage">
  <section class="card card--front">
    <div class="brand">
      <span class="brand__dot"></span>
      <span class="brand__name">PeppertonRUN</span>
    </div>
    <p class="tagline">Fitness, Nutrition &amp; Wellness</p>
  </section>

  <section class="card card--back">
    <div class="card__ghost-mark"></div>
    <div class="identity">
      <h1 class="identity__name">Mara Dulvik Tenbrook</h1>
      <p class="identity__role">FOUNDER</p>
    </div>
    <ul class="contact">
      <li class="contact__item">
        <svg class="contact__icon" viewBox="0 0 24 24"><path d="M6.6 10.8a15 15 0 0 0 6.6 6.6l2.2-2.2a1 1 0 0 1 1-.25 11.4 11.4 0 0 0 3.6.57 1 1 0 0 1 1 1V20a1 1 0 0 1-1 1A17 17 0 0 1 3 4a1 1 0 0 1 1-1h3.5a1 1 0 0 1 1 1c0 1.25.2 2.45.57 3.57a1 1 0 0 1-.25 1z"/></svg>
        718-555-0143
      </li>
      <li class="contact__item">
        <svg class="contact__icon" viewBox="0 0 24 24"><path d="M12 2a10 10 0 1 0 0 20 10 10 0 0 0 0-20zm6.9 6h-2.9a15.6 15.6 0 0 0-1.4-3.6A8 8 0 0 1 18.9 8zM12 4c.8 1.2 1.5 2.5 1.9 4h-3.8c.4-1.5 1.1-2.8 1.9-4zM4.3 14a8 8 0 0 1 0-4h3.4a16 16 0 0 0 0 4zm.8 2h2.9c.3 1.3.8 2.5 1.4 3.6A8 8 0 0 1 5.1 16zM8 8H5.1a8 8 0 0 1 4.3-3.6C8.8 5.5 8.3 6.7 8 8zm4 12c-.8-1.2-1.5-2.5-1.9-4h3.8c-.4 1.5-1.1 2.8-1.9 4zm2.3-6H9.7a14.7 14.7 0 0 1 0-4h4.6a14.7 14.7 0 0 1 0 4zm.3 5.6c.6-1.1 1.1-2.3 1.4-3.6h2.9a8 8 0 0 1-4.3 3.6zm1.7-5.6a16 16 0 0 0 0-4h3.4a8 8 0 0 1 0 4z"/></svg>
        www.peppertonrun.com
      </li>
      <li class="contact__item">
        <svg class="contact__icon" viewBox="0 0 24 24"><path d="M2 5h20v14H2z M2 5l10 8 10-8" stroke="#262626" stroke-width="1.5"/></svg>
        mara@peppertonrun.com
      </li>
    </ul>
    <div class="card__stripe"></div>
  </section>
</main>
</body>
</html>
```